Banner Design

A law firm looking for a logo that can be used in a web banner that highlights the web address "splitpathcounsel.net" and incorporates our law firms name- Brantley and Associates. Would prefer a design with softer green color like Russian Green.

A preliminary thought would be a boxed banner with a Brantley and Associates logo on either side of the web address "splitpathcounsel.net".

Traditional and modern designs welcomed.
Updates

   Please make sure that "splitpathcounsel.net" is the main focus of the banner.  All advertising is being done to brand that website address.  Our law firm name/logo needs to be incorporated but not the focal point.  This banner will be listed at the top of every web page.

Designers feel free to go with an over/under design with splitpathcounsel.net going on top in a prominent position over our firm name. If that style sparks your creativity.  Remember this will be the banner design that will go on top of every page of the new website.        

                                I was thinking the firm name/logo on either side of the "splitpathcounsel.net" would look balanced. But from the designs that I have received maybe it would look more balance with the "splitpathcounsel.net" illustration over the firm name.

Target Market(s)

individuals 30-50

Industry/Entity Type

Law Firm

Logo Text

Brantley and Associates splitpathcounsel.net

Logo styles of interest
Emblem Logo
Wordmark Logo

```html
<!DOCTYPE html>
<html lang="en">
<head>
<meta charset="utf-8">
<title>Brantley and Associates — splitpathcounsel.net banner</title>
<link href="https://fonts.googleapis.com/css2?family=Varela+Round&family=Open+Sans:wght@600&display=swap" rel="stylesheet">
<style>
  :root {
    --russian-green: #3c7d5c;
    --headline-green: #3f8c62;
    --panel-white: #ffffff;
    --panel-grey: #e6e8e7;
    --badge-teal: #22b3d6;
    --name-dark: #3d3d3d;
    --name-light: #ffffff;
    --scale-bronze: #8a6a3a;
    --scale-light: #e9e2d3;
  }
  html, body {
    margin: 0;
    padding: 0;
    overflow: hidden;
    background: #ffffff;
  }
  .banner {
    position: relative;
    width: 1200px;
    height: 148px;
    overflow: hidden;
    background: linear-gradient(180deg, var(--panel-white) 0%, var(--panel-white) 55%, var(--panel-grey) 100%);
  }
  .banner__shapes {
    position: absolute;
    inset: 0;
    width: 1200px;
    height: 148px;
  }
  .banner__scales {
    position: absolute;
    left: 915px;
    top: 0;
    width: 150px;
    height: 148px;
    background: radial-gradient(ellipse at 50% 55%, var(--scale-bronze) 0%, #b49560 35%, var(--scale-light) 70%, rgba(255,255,255,0) 100%);
  }
  .firm {
    position: absolute;
    display: flex;
    flex-direction: column;
    align-items: center;
    gap: 6px;
    font-family: "Open Sans", sans-serif;
    font-weight: 600;
    font-size: 11px;
    white-space: nowrap;
  }
  .firm__badge {
    width: 42px;
    height: 42px;
    border-radius: 50%;
    background: var(--badge-teal);
  }
  .firm--left {
    left: 115px;
    top: 28px;
    transform: translateX(-50%);
    color: var(--name-light);
  }
  .firm--right {
    left: 1120px;
    top: 44px;
    transform: translateX(-50%);
    color: var(--name-dark);
  }
  .web-address {
    position: absolute;
    left: 262px;
    top: 36px;
    margin: 0;
    font-family: "Varela Round", sans-serif;
    font-weight: 400;
    font-size: 58px;
    line-height: 1;
    letter-spacing: 0.5px;
    color: var(--headline-green);
  }
</style>
</head>
<body>
<div class="banner">
  <svg class="banner__shapes" viewBox="0 0 728 90" preserveAspectRatio="none" aria-hidden="true">
    <polygon class="band-left" points="0,0 345,0 333,8 160,8 128,90 0,90" fill="var(--russian-green)"/>
    <polygon class="corner-top-right" points="600,0 728,0 728,28 690,28" fill="var(--russian-green)"/>
    <polygon class="corner-bottom-right" points="700,90 728,90 728,62" fill="var(--russian-green)"/>
  </svg>

  <div class="banner__scales" role="img" aria-label="Photograph of bronze scales of justice"></div>

  <div class="firm firm--left">
    <span class="firm__badge"></span>
    <span class="firm__name">Brantley and Associates</span>
  </div>

  <h1 class="web-address">splitpathcounsel.net</h1>

  <div class="firm firm--right">
    <span class="firm__badge"></span>
    <span class="firm__name">Brantley and Associates</span>
  </div>
</div>
</body>
</html>
```